"Cork Hollow Excursions" is a top notch Santa Barbara County Wine Tour company.

We provide scenic, boutique and custom wine tours. I need the card to be clean and classy. I will provide our logo. I would like the logo to cover the back side of the card as an option and would like to see a couple color options other then our signature green and gold. I would like to see some creative options and let the designers come up with options.
I need cards for myself and my team. The final design should communicate "An authentic and boutique wine tour experience"
Please use my website for reference www.corkhollowexcursions.com

Target Market(s)

We have a wide range of clients from millennials to baby boomers

Industry/Entity Type

Tour

Contact Information for Business Card

Contact info:
Dale Munford
805-291-6384
info@corkhollowexcursions.com
corkhollowexcursions.com

Colors

Designer to choose colors to be used in the design.

Requirements
Must have
• my logo
Nice to have
• *I would like to have the backside side with the logo and the company statement
• "An authentic and boutique wine tour experience" as an option.
• *I would also like to see what the designers can create!
• *I would like to see an option that incorporates or social: snapgrid, rovia, route scout
Should not have
• I do not want it too busy.

```html
<!DOCTYPE html>
<html lang="en">
<head>
<meta charset="utf-8">
<title>Cork Hollow Excursions — Business Cards</title>
<link href="https://fonts.googleapis.com/css2?family=Open+Sans:wght@400;600;700&display=swap" rel="stylesheet">
<style>
  :root {
    --backdrop: #cfcfd2;
    --card: #151515;
    --card-edge: #0b0b0b;
    --ink-light: #f2f2f2;
    --ink-soft: #bdbdbd;
    --green: #2f7d46;
    --gold: #b9a07c;
    --rule: #8a8a8a;
  }
  * { margin: 0; padding: 0; box-sizing: border-box; }
  html, body {
    width: 1200px; height: 1023px; overflow: hidden;
    background: var(--backdrop);
    font-family: "Open Sans", Arial, sans-serif;
  }
  .sheet {
    width: 1200px; height: 1023px;
    display: flex; flex-direction: column; align-items: center; justify-content: center;
    gap: 44px;
  }
  .card {
    position: relative;
    width: 770px; height: 440px;
    background: var(--card);
    border-bottom: 4px solid var(--card-edge);
    box-shadow: 0 12px 28px rgba(0,0,0,0.35);
    overflow: hidden;
  }

  /* Front */
  .front { display: flex; flex-direction: column; align-items: center; justify-content: center; }
  .front .brand-name {
    color: var(--ink-light); font-weight: 600; font-size: 50px;
    letter-spacing: 3px; text-transform: uppercase; text-align: center; line-height: 1.1;
  }
  .front .region {
    display: flex; align-items: center; gap: 18px;
    margin-top: 16px; color: var(--ink-light);
    font-size: 17px; letter-spacing: 9px; text-transform: uppercase;
  }
  .region .dash { width: 60px; height: 2px; background: var(--ink-light); }
  .socials {
    display: flex; align-items: center; gap: 22px; margin-top: 34px;
  }
  .socials .dash { width: 40px; height: 2px; background: var(--ink-light); }
  .social { display: flex; align-items: center; gap: 7px; color: var(--ink-light); font-size: 14px; }
  .social .dot { width: 16px; height: 16px; border-radius: 50%; background: var(--ink-light); }

  /* Back */
  .back .brand {
    position: absolute; left: 56px; top: 56px; width: 340px;
  }
  .back .brand-name {
    color: var(--gold); font-weight: 600; font-size: 34px;
    letter-spacing: 2px; text-transform: uppercase; line-height: 1.15;
  }
  .back .region {
    margin-top: 12px; color: var(--green);
    font-size: 13px; letter-spacing: 7px; text-transform: uppercase;
  }
  .divider { position: absolute; left: 0; top: 0; }
  .contact {
    position: absolute; left: 430px; top: 190px;
  }
  .contact .person {
    color: var(--green); font-weight: 700; font-size: 28px; letter-spacing: 1px; margin-bottom: 14px;
  }
  .contact ul { list-style: none; }
  .contact li {
    display: flex; align-items: center; gap: 12px;
    color: var(--ink-light); font-size: 19px; line-height: 1.55; letter-spacing: 0.5px;
  }
  .contact svg { width: 16px; height: 16px; flex: none; }
  .tagline {
    position: absolute; left: 40px; right: 40px; bottom: 34px;
    display: flex; align-items: center; justify-content: center; gap: 16px;
    color: var(--ink-light); font-size: 17px; letter-spacing: 0.6px;
  }
  .tagline .dash { width: 30px; height: 2px; background: var(--ink-light); }
</style>
</head>
<body>
<main class="sheet">

  <section class="card front" aria-label="Card front">
    <h1 class="brand-name">Cork Hollow<br>Excursions</h1>
    <p class="region"><span class="dash"></span>Santa Barbara County<span class="dash"></span></p>
    <div class="socials">
      <span class="dash"></span>
      <span class="social"><span class="dot"></span>friendwall</span>
      <span class="social"><span class="dot"></span>snapgrid</span>
      <span class="social"><span class="dot"></span>rovia</span>
      <span class="social"><span class="dot"></span>route scout</span>
      <span class="dash"></span>
    </div>
  </section>

  <section class="card back" aria-label="Card back">
    <div class="brand">
      <h2 class="brand-name">Cork Hollow<br>Excursions</h2>
      <p class="region">Santa Barbara County</p>
    </div>

    <svg class="divider" width="770" height="440" viewBox="0 0 770 440" aria-hidden="true">
      <defs>
        <linearGradient id="rule-fade" x1="0" y1="0" x2="1" y2="0">
          <stop offset="0" stop-color="#cfcfcf" stop-opacity="0"/>
          <stop offset="0.5" stop-color="#cfcfcf" stop-opacity="0.9"/>
          <stop offset="1" stop-color="#cfcfcf" stop-opacity="0"/>
        </linearGradient>
      </defs>
      <line x1="330" y1="325" x2="420" y2="40" stroke="url(#rule-fade)" stroke-width="2"/>
    </svg>

    <div class="contact">
      <p class="person">Dale Munford</p>
      <ul>
        <li>
          <svg viewBox="0 0 16 16" aria-hidden="true"><circle cx="8" cy="8" r="7" fill="none" stroke="#f2f2f2" stroke-width="1.4"/><path d="M5.5 4.5l1.5 0 0.7 2-1 0.8a5 5 0 0 0 2 2l0.8-1 2 0.7 0 1.5c-4 0.6-7-2.6-6-6z" fill="#f2f2f2"/></svg>
          805-291-6384
        </li>
        <li>
          <svg viewBox="0 0 16 16" aria-hidden="true"><rect x="1" y="3" width="14" height="10" fill="#2f7d46"/><path d="M1 3l7 6 7-6" fill="none" stroke="#151515" stroke-width="1.3"/></svg>
          info@corkhollowexcursions.com
        </li>
        <li>
          <svg viewBox="0 0 16 16" aria-hidden="true"><circle cx="8" cy="8" r="7.5" fill="#2f7d46"/><path d="M0.5 8h15M8 0.5c-3 3-3 12 0 15M8 0.5c3 3 3 12 0 15" fill="none" stroke="#151515" stroke-width="1"/></svg>
          www.corkhollowexcursions.com
        </li>
      </ul>
    </div>

    <p class="tagline"><span class="dash"></span>An authentic and boutique wine tour experience<span class="dash"></span></p>
  </section>

</main>
</body>
</html>
```